Visitenkarten-Design für Yogakurse
Zielgruppe
Ich biete Yogakurse für alle an sowieso speziell Yogakurse für Schwangere, frischgebackene Mamas und Rückbildungskurse.
Meine Zielgruppe sind hauptsächlich schwangere Frauen sowieso Frauen mit Babys.
Aufgabenstellung
Folgende Informationen sollten enthalten sein:
Ruhe im Atem
Yoga & Beckenbodentraining
Henrike Wolmsen
info@ruhe-im-atem-beispiel.de
www.ruhe-im-atem-beispiel.de

```html
<!DOCTYPE html>
<html lang="de">
<head>
<meta charset="utf-8">
<title>Ruhe im Atem – Visitenkarten</title>
<link rel="stylesheet" href="https://fonts.googleapis.com/css2?family=Caveat+Brush&family=Montserrat:wght@400;500&display=swap">
<style>
  :root {
    --stage: #c8c8c8;
    --card: #d8e5c7;
    --gold: #bb8638;
    --gold-soft: #d5b46c;
    --gold-pale: #e2cc8e;
  }
  * { box-sizing: border-box; margin: 0; padding: 0; }
  html, body { width: 1200px; height: 800px; overflow: hidden; }
  body { background: var(--stage); position: relative; font-family: "Montserrat", sans-serif; color: var(--gold); }

  .card {
    position: absolute; top: 340px; width: 480px; height: 275px;
    background: var(--card); overflow: hidden;
  }
  .card--front { left: 97px; }
  .card--back { left: 620px; }

  .card__waves { position: absolute; inset: 0; width: 100%; height: 100%; }

  .brand {
    position: absolute; display: flex; align-items: center; gap: 6px;
    font-family: "Montserrat", sans-serif; font-weight: 500; color: var(--gold);
    white-space: nowrap;
  }
  .brand__dot { width: 9px; height: 9px; border-radius: 50%; background: var(--gold); }
  .card--front .brand { left: 14px; top: 58px; font-size: 16px; }
  .card--back .brand { left: 50%; top: 112px; transform: translateX(-50%); font-size: 18px; }

  .tagline {
    position: absolute; left: 150px; width: 325px; top: 70px;
    font-family: "Caveat Brush", cursive; font-size: 40px; line-height: 1.05;
    text-align: center; color: var(--gold);
  }
  .tagline span { display: block; }
  .tagline .tagline__amp { font-size: 32px; }

  .person { position: absolute; left: 33px; top: 170px; }
  .person__name { font-size: 23px; font-weight: 500; letter-spacing: 0.2px; }
  .person__role { margin-top: 6px; font-size: 12.5px; font-weight: 400; letter-spacing: 0.3px; }

  .divider { position: absolute; left: 258px; top: 170px; width: 1px; height: 62px; background: var(--gold); }

  .contact { position: absolute; left: 270px; top: 172px; list-style: none; }
  .contact li { display: flex; align-items: center; gap: 7px; height: 23px; font-size: 10.5px; }
  .contact svg { width: 10px; height: 10px; flex: none; }
</style>
</head>
<body>

<section class="card card--front">
  <svg class="card__waves" viewBox="0 0 480 275" role="img" aria-label="Weiche goldene Wellenbänder am unteren Rand">
    <defs>
      <linearGradient id="frontWave" x1="0" y1="0" x2="1" y2="0">
        <stop offset="0" stop-color="var(--gold-soft)"/>
        <stop offset="0.5" stop-color="var(--gold-pale)"/>
        <stop offset="1" stop-color="var(--gold-soft)"/>
      </linearGradient>
    </defs>
    <path d="M0 130 C90 150 160 210 200 245 C280 225 360 205 480 232 L480 275 L0 275 Z" fill="url(#frontWave)" opacity="0.85"/>
  </svg>
  <div class="brand"><span class="brand__dot"></span>Ruhe im Atem</div>
  <h1 class="tagline">
    <span>Yoga</span>
    <span class="tagline__amp">&amp;</span>
    <span>Beckenbodentraining</span>
  </h1>
</section>

<section class="card card--back">
  <svg class="card__waves" viewBox="0 0 480 275" role="img" aria-label="Weiche goldene Wellenbänder oben und rechts">
    <defs>
      <linearGradient id="backWave" x1="0" y1="0" x2="1" y2="1">
        <stop offset="0" stop-color="var(--gold-pale)"/>
        <stop offset="0.6" stop-color="var(--gold-soft)"/>
        <stop offset="1" stop-color="var(--gold-pale)"/>
      </linearGradient>
    </defs>
    <path d="M0 0 L480 0 L480 160 C420 110 360 40 260 25 C200 20 160 35 110 55 C70 68 30 65 0 55 Z" fill="url(#backWave)" opacity="0.85"/>
  </svg>
  <div class="brand"><span class="brand__dot"></span>Ruhe im Atem</div>

  <div class="person">
    <h2 class="person__name">Henrike Wolmsen</h2>
    <p class="person__role">Yoga &amp; Beckenbodentraining</p>
  </div>

  <div class="divider"></div>

  <ul class="contact">
    <li>
      <svg viewBox="0 0 24 24" fill="var(--gold)" aria-hidden="true"><path d="M6.6 10.8a15.2 15.2 0 0 0 6.6 6.6l2.2-2.2a1 1 0 0 1 1-.25 11.4 11.4 0 0 0 3.6.57 1 1 0 0 1 1 1V20a1 1 0 0 1-1 1A17 17 0 0 1 3 4a1 1 0 0 1 1-1h3.5a1 1 0 0 1 1 1c0 1.25.2 2.45.57 3.57a1 1 0 0 1-.25 1z"/></svg>
      0176 - 4830915
    </li>
    <li>
      <svg viewBox="0 0 24 24" fill="var(--gold)" aria-hidden="true"><path d="M2 5h20v14H2z M2 5l10 8 10-8" stroke="var(--card)" stroke-width="1.5"/></svg>
      info@ruhe-im-atem-beispiel.de
    </li>
    <li>
      <svg viewBox="0 0 24 24" fill="none" stroke="var(--gold)" stroke-width="1.6" aria-hidden="true"><circle cx="12" cy="12" r="10"/><ellipse cx="12" cy="12" rx="4.5" ry="10"/><path d="M2 12h20M4 7h16M4 17h16"/></svg>
      www.ruhe-im-atem-beispiel.de
    </li>
  </ul>
</section>

</body>
</html>
```